Podcast Cover Design - Tiding For Level Heads

We renamed our podcast from the "Harborline Property Hour Podcast" to "Tidings For Level Heads" and we need a new podcast cover design, Instagram profile picture, and a YouTube banner.

More so we're looking for some sort of symbol/icon. Our old logo had the Cobalt Spire but we're moving to a much broader audience that isn't necessarily from Seattle and needs something that will appeal to them.

In the podcast, Doran reads the news that big media isn't covering including crime, business, homeless crisis, protests. We stay away from covering politics but our audience is mainly right-wing.

Attached are some additional designs we created in-house.

If we love the design we'll have additional job opportunities to create possible designs for merchandise.

Target Market(s)

80% Males aged 50+, Republican

Industry/Entity Type

News

Colors

Designer to choose colors to be used in the design.

Requirements
Must have
• OPEN TOO IDEAS
Nice to have
• OPEN TOO IDEAS
Should not have
• Cobalt Spire

```html
<!DOCTYPE html>
<html lang="en">
<head>
<meta charset="utf-8">
<title>Tidings For Level Heads – Podcast Cover</title>
<link rel="stylesheet" href="https://fonts.googleapis.com/css2?family=Bebas+Neue&family=Oswald:wght@300;400&family=Outfit:wght@400;700&display=swap">
<style>
  :root {
    --wall-dark: #141414;
    --wall-mid: #2c2c2c;
    --brand-red: #c81c1f;
    --ink-white: #ffffff;
    --portrait-light: #9a9a9a;
    --portrait-dark: #3a3a3a;
  }
  html, body {
    margin: 0;
    padding: 0;
    width: 1200px;
    height: 1200px;
    overflow: hidden;
    background: var(--wall-dark);
  }
  .cover {
    position: relative;
    width: 1200px;
    height: 1200px;
    overflow: hidden;
  }
  .wall-backdrop {
    position: absolute;
    inset: 0;
    background: radial-gradient(ellipse at 45% 40%, var(--wall-mid) 0%, var(--wall-dark) 75%);
  }
  .cover-art {
    position: absolute;
    inset: 0;
  }
  .title-word {
    font-family: "Bebas Neue", "Oswald", sans-serif;
    fill: var(--ink-white);
  }
  .title-joiner {
    font-family: "Bebas Neue", "Oswald", sans-serif;
    fill: var(--brand-red);
  }
  .host-credit {
    position: absolute;
    left: 89px;
    top: 918px;
    margin: 0;
    color: var(--ink-white);
    font-family: "Outfit", sans-serif;
    font-size: 34px;
    line-height: 1;
    white-space: nowrap;
  }
  .host-credit .by { font-weight: 400; }
  .host-credit .host-name {
    font-weight: 700;
    font-size: 44px;
    letter-spacing: -0.5px;
  }
  .format-label {
    position: absolute;
    left: 89px;
    top: 1088px;
    margin: 0;
    color: var(--ink-white);
    font-family: "Oswald", sans-serif;
    font-weight: 300;
    font-size: 31px;
    letter-spacing: 12px;
    line-height: 1;
  }
</style>
</head>
<body>
  <main class="cover">
    <div class="wall-backdrop" role="img" aria-label="Dark black brick wall texture"></div>

    <svg class="cover-art" width="1200" height="1200" viewBox="0 0 1200 1200" xmlns="http://www.w3.org/2000/svg">
      <!-- title band -->
      <rect class="title-band" x="89" y="594" width="740" height="275" fill="var(--brand-red)"/>

      <!-- host portrait cut-out -->
      <path class="host-portrait" role="img" aria-label="Black and white posterized portrait of the host, Doran, in a patterned jacket"
        d="M1200,160 L1200,1200 L267,1200 C360,1130 470,1040 560,990 C610,965 640,975 680,940
           C740,900 800,880 825,860 L810,760 C790,700 770,640 760,590 C745,545 752,500 764,470
           C760,420 770,330 805,270 C850,190 930,125 1022,109 C1090,100 1150,120 1180,150 Z"
        fill="url(#portraitTone)" stroke="var(--brand-red)" stroke-width="4"/>
      <defs>
        <linearGradient id="portraitTone" x1="0" y1="0" x2="1" y2="1">
          <stop offset="0" stop-color="var(--portrait-light)"/>
          <stop offset="1" stop-color="var(--portrait-dark)"/>
        </linearGradient>
      </defs>

      <!-- title -->
      <text class="title-word" x="89" y="393" font-size="372" textLength="617" lengthAdjust="spacingAndGlyphs">TIDINGS</text>
      <text class="title-joiner" x="89" y="462" font-size="84" textLength="100" lengthAdjust="spacingAndGlyphs">FOR</text>
      <text class="title-word" x="89" y="548" font-size="152" textLength="617" lengthAdjust="spacing">LEVEL</text>
      <text class="title-word" x="121" y="825" font-size="265" textLength="585" lengthAdjust="spacing">HEADS</text>
    </svg>

    <p class="host-credit"><span class="by">by</span> <span class="host-name">DORAN WHITLOCK</span></p>
    <p class="format-label">PODCAST</p>
  </main>
</body>
</html>
```